Easter & Summer School Dance Camps

I need two flyers one for Easter camps and one for summer school
We are a performing arts and dance academy

I want a double sided flyers one side summer school one side easter camp

Please make these flyers appeal to young dancers and performers - eye catching up to date Added Tuesday, March 1, 2016

Target Market(s)

Young children and teenagers

Industry/Entity Type

School

Font styles to use
Serif
Sans Serif

Requirements
Must have
• bright colourful

```html
<!DOCTYPE html>
<html lang="en">
<head>
<meta charset="utf-8">
<title>Brightstage Summer School</title>
<link href="https://fonts.googleapis.com/css2?family=Baskervville&family=Libre+Baskerville:wght@400;700&display=swap" rel="stylesheet">
<style>
  :root {
    --orange: #f7941d;
    --ink: #1a1a1a;
    --paper: #ffffff;
    --pink: #d6359a;
    --pink-light: #ec8ac3;
    --teal: #3dbfb0;
    --teal-light: #9fe0d8;
    --star-deep: #f2602a;
    --star-light: #fbb03b;
    --berry: #c63a55;
    --cone: #b07a4a;
  }
  * { margin: 0; padding: 0; box-sizing: border-box; }
  html, body { width: 847px; height: 1200px; overflow: hidden; background: var(--paper); }
  .flyer {
    position: relative;
    width: 847px;
    height: 1200px;
    overflow: hidden;
    background: var(--paper);
    color: var(--ink);
    font-family: "Baskervville", "Libre Baskerville", serif;
    text-align: center;
  }

  /* brand */
  .brand {
    position: absolute;
    top: 66px;
    left: 0;
    width: 100%;
    display: flex;
    justify-content: center;
    align-items: center;
    gap: 8px;
    font-family: "Baskervville", serif;
    font-size: 40px;
    color: var(--ink);
    line-height: 1;
  }
  .brand-dot {
    width: 12px; height: 12px; border-radius: 50%;
    background: var(--pink);
  }

  /* headings */
  .kicker {
    position: absolute;
    top: 202px;
    left: 0; width: 100%;
    font-family: "Libre Baskerville", serif;
    font-weight: 400;
    font-size: 29px;
    line-height: 35px;
    letter-spacing: 3px;
    color: var(--orange);
  }
  .title {
    position: absolute;
    top: 290px;
    left: 0; width: 100%;
    font-family: "Libre Baskerville", serif;
    font-weight: 700;
    font-size: 81px;
    line-height: 92px;
    color: var(--orange);
  }

  /* details */
  .details {
    position: absolute;
    top: 538px;
    left: 0; width: 100%;
    font-size: 18.5px;
    line-height: 24px;
  }
  .details .dates { font-weight: 700; font-family: "Libre Baskerville", serif; font-size: 17px; }

  .body-copy {
    position: absolute;
    top: 634px;
    left: 0; width: 100%;
    font-size: 18.5px;
    line-height: 24px;
  }
  .body-copy p { margin-bottom: 24px; }

  .contact {
    position: absolute;
    top: 950px;
    left: 0; width: 100%;
    font-size: 17.5px;
    line-height: 24px;
    letter-spacing: 0.6px;
  }

  /* decorative artwork areas */
  .art { position: absolute; }
  .star-left-top { left: -20px; top: 86px; width: 136px; height: 176px; background: linear-gradient(135deg, var(--star-light), var(--star-deep)); clip-path: polygon(0 0, 20% 0, 100% 50%, 40% 100%, 0 100%); }
  .lollies { left: 640px; top: 0; width: 184px; height: 132px; background: linear-gradient(90deg, var(--pink-light), var(--teal)); border-radius: 0 0 40px 40px; }
  .star-right { left: 738px; top: 256px; width: 109px; height: 144px; background: linear-gradient(160deg, var(--star-light), var(--star-deep) 55%, #f39a86); clip-path: polygon(30% 0, 100% 5%, 100% 100%, 0 35%); }
  .mic-left { left: -10px; top: 484px; width: 170px; height: 92px; background: linear-gradient(90deg, var(--pink), var(--pink-light)); border-radius: 20px 46px 46px 20px; clip-path: polygon(0 60%, 45% 20%, 60% 0, 100% 0, 100% 100%, 55% 100%, 0 95%); }
  .mic-right { left: 716px; top: 586px; width: 140px; height: 94px; background: linear-gradient(90deg, var(--pink-light), var(--pink)); border-radius: 47px 10px 10px 47px; }
  .star-left-bottom { left: 0; top: 796px; width: 100px; height: 204px; background: linear-gradient(180deg, var(--star-deep), var(--star-light) 35%, #f39a86); clip-path: polygon(0 10%, 60% 0, 100% 30%, 30% 100%, 0 100%); }
  .icecream-right { left: 736px; top: 852px; width: 111px; height: 136px; background: linear-gradient(160deg, var(--berry), var(--cone)); border-radius: 50% 50% 20% 20%; }
  .icecreams-bottom { left: 256px; top: 1068px; width: 336px; height: 132px; background: linear-gradient(90deg, var(--teal), var(--pink) 50%, var(--teal)); border-radius: 60px 60px 0 0; }
</style>
</head>
<body>
<main class="flyer">
  <div class="art star-left-top" role="img" aria-label="Orange shooting star illustration"></div>
  <div class="art lollies" role="img" aria-label="Pink and teal ice lolly illustration"></div>
  <div class="art star-right" role="img" aria-label="Orange shooting star with trail illustration"></div>
  <div class="art mic-left" role="img" aria-label="Pink microphone illustration"></div>
  <div class="art mic-right" role="img" aria-label="Pink microphone illustration"></div>
  <div class="art star-left-bottom" role="img" aria-label="Orange shooting star with trail illustration"></div>
  <div class="art icecream-right" role="img" aria-label="Berry ice cream cone illustration"></div>
  <div class="art icecreams-bottom" role="img" aria-label="Row of teal and pink ice cream cones illustration"></div>

  <header class="brand">
    <span class="brand-dot"></span>
    <span class="brand-name">Brightstage</span>
  </header>

  <h2 class="kicker">BRIGHTSTAGE<br>SUMMER SCHOOL</h2>
  <h1 class="title">A Wicked<br>West End Wiz</h1>

  <section class="details">
    <div class="dates">8 August – 12 August 2016</div>
    <div class="times">10 a.m. – 4 p.m.</div>
    <div class="price">150.00</div>
  </section>

  <section class="body-copy">
    <p>Summer school is designed for young people who enjoy performing.<br>The course introduces you to various disciplines of theatre:<br>Acting, Singing and Dance.</p>
    <p>Everyone is able to develop at their own pace, no-one is forced to perform<br>and there are opportunities for you to explore performance techniques.</p>
    <p>Students will develop key skills in teamwork, communication<br>and confidence whilst building friendships and having fun!<br>The week ends with a showing, to friends and family, of the<br>skills and musical numbers achieved during the course.</p>
  </section>

  <footer class="contact">
    <div>Venue: The Parish Hall of St Aldric Elmbridge Vale KT9 4XR</div>
    <div>Email: brightstagebookings@gmail to book or text 07700900123</div>
  </footer>
</main>
</body>
</html>
```